Rare Plume Edibles Gummies

Packaging design for custom mylars for cannabis infused gummies. I need a space for a warning label, nutrition facts, ingredients, brand logo and then individualized item details. We will later be doing assorted peanut butter cups, hard candies, etc.

```html
<!DOCTYPE html>
<html lang="en">
<head>
<meta charset="utf-8">
<title>Rare Plume Edibles Gummies – Pouch Front and Back</title>
<link rel="stylesheet" href="https://fonts.googleapis.com/css2?family=Nunito:wght@400;600;700;800&family=Exo+2:ital,wght@1,600&family=Kaushan+Script&display=swap">
<style>
  :root {
    --page: #ffffff;
    --pouch-deep: #2c48a8;
    --pouch-light: #4a6bd0;
    --seal-line: rgba(15, 30, 90, 0.35);
    --ink: #ffffff;
    --ink-soft: rgba(255, 255, 255, 0.85);
    --gummy-a: #5cc3e6;
    --gummy-b: #1d4f8a;
    --berry: #3b46b8;
  }
  * { box-sizing: border-box; margin: 0; padding: 0; }
  html, body { width: 1200px; height: 835px; overflow: hidden; background: var(--page); }
  body { position: relative; font-family: "Nunito", sans-serif; color: var(--ink); }

  .pouch {
    position: absolute; top: 160px; width: 315px; height: 547px;
    background: var(--pouch-deep);
    border-radius: 12px 12px 4px 4px;
    overflow: hidden;
  }
  .pouch--front { left: 227px; }
  .pouch--back { left: 697px; }

  .pouch__seal { position: absolute; left: 0; right: 0; top: 52px; height: 1px; background: var(--seal-line); }
  .pouch__zipper {
    position: absolute; left: 16px; right: 16px; top: 62px; height: 10px;
    border-top: 2px solid var(--seal-line); border-bottom: 1px solid var(--seal-line);
  }
  .pouch__notch { position: absolute; top: 34px; width: 4px; height: 4px; background: var(--page); border-radius: 50%; }
  .pouch__notch--l { left: -2px; }
  .pouch__notch--r { right: -2px; }

  .pouch__wave { position: absolute; left: 0; top: 0; width: 315px; height: 547px; }

  .brand {
    position: absolute; border: 1.5px solid var(--ink-soft); border-radius: 50%;
    display: flex; flex-direction: column; align-items: center; justify-content: center;
    font-family: "Nunito", sans-serif; font-weight: 700; color: var(--ink); text-align: center; line-height: 1.05;
  }
  .brand--front { left: 46px; top: 136px; width: 152px; height: 152px; font-size: 22px; }
  .brand--back { left: 167px; top: 441px; width: 104px; height: 104px; font-size: 15px; }

  /* front */
  .gummy-photo {
    position: absolute; left: 43px; top: 298px; width: 232px; height: 168px;
    background: radial-gradient(circle at 60% 45%, var(--gummy-a), var(--gummy-b) 85%);
    border-radius: 30px 0 0 0;
  }
  .flavor { position: absolute; left: 26px; top: 478px; display: flex; align-items: center; gap: 8px; }
  .flavor__berries { width: 44px; height: 38px; border-radius: 50%; background: var(--berry); }
  .flavor__name { font-family: "Kaushan Script", cursive; font-size: 20px; color: var(--ink); }
  .potency { position: absolute; right: 28px; top: 524px; font-size: 8px; font-weight: 800; letter-spacing: 0.6px; }

  /* back */
  .claims {
    position: absolute; left: 22px; top: 154px; width: 290px;
    font-family: "Exo 2", sans-serif; font-style: italic; font-weight: 600; font-size: 11.5px; line-height: 1.4;
  }
  .notice { position: absolute; left: 25px; width: 120px; }
  .notice--warning { top: 238px; }
  .notice--dosing { top: 346px; }
  .notice__title { font-size: 13px; font-weight: 800; margin-bottom: 3px; }
  .notice__body { font-size: 8px; font-weight: 600; line-height: 1.45; color: var(--ink-soft); }
  .ingredients {
    position: absolute; left: 33px; top: 480px; width: 110px;
    font-size: 7.5px; font-weight: 700; line-height: 1.4; text-transform: uppercase;
  }

  .nutrition {
    position: absolute; left: 152px; top: 203px; width: 131px;
    border: 1px solid var(--ink); padding: 2px 3px; font-size: 6px; line-height: 1.35;
  }
  .nutrition__title { font-size: 13px; font-weight: 800; line-height: 1; border-bottom: 1px solid var(--ink); padding-bottom: 1px; }
  .nutrition__row { display: flex; justify-content: space-between; border-bottom: 0.5px solid var(--ink-soft); }
  .nutrition__row--indent { padding-left: 7px; }
  .nutrition__row--thick { border-bottom: 3px solid var(--ink); }
  .nutrition__cal { display: flex; justify-content: space-between; align-items: flex-end; font-weight: 800; font-size: 10px; border-bottom: 2px solid var(--ink); }
  .nutrition__cal strong { font-size: 14px; }
  .nutrition__dv { text-align: right; font-size: 5px; border-bottom: 0.5px solid var(--ink-soft); }
  .nutrition__foot { font-size: 4px; line-height: 1.3; padding-top: 2px; }
</style>
</head>
<body>

<section class="pouch pouch--front" aria-label="Pouch front">
  <svg class="pouch__wave" viewBox="0 0 315 547" aria-hidden="true">
    <path d="M0 330 C 80 300, 160 280, 240 295 C 280 302, 300 300, 315 296 L 315 547 L 0 547 Z" fill="var(--pouch-light)" opacity="0.55"/>
  </svg>
  <span class="pouch__notch pouch__notch--l"></span><span class="pouch__notch pouch__notch--r"></span>
  <div class="pouch__seal"></div>
  <div class="pouch__zipper"></div>

  <div class="brand brand--front"><span>Rare Plume</span><span>Edibles</span></div>

  <div class="gummy-photo" role="img" aria-label="Photo of sugar-coated blue raspberry gummies"></div>

  <div class="flavor">
    <div class="flavor__berries" role="img" aria-label="Illustration of blue raspberries"></div>
    <span class="flavor__name">Blue Raspberry Flavor</span>
  </div>
  <p class="potency">20MG D8 PER PIECE</p>
</section>

<section class="pouch pouch--back" aria-label="Pouch back">
  <svg class="pouch__wave" viewBox="0 0 315 547" aria-hidden="true">
    <path d="M0 225 C 70 240, 150 210, 215 200 C 260 193, 295 195, 315 200 L 315 547 L 0 547 Z" fill="var(--pouch-light)" opacity="0.6"/>
  </svg>
  <span class="pouch__notch pouch__notch--l"></span><span class="pouch__notch pouch__notch--r"></span>
  <div class="pouch__seal"></div>
  <div class="pouch__zipper"></div>

  <p class="claims">LAB TESTED FOR QUALITY AND CONSISTENCY<br>INFUSED WITH SOLVENT FREE HEMP DISTILLATE</p>

  <div class="notice notice--warning">
    <h2 class="notice__title">WARNING:</h2>
    <p class="notice__body">The intoxicating effects of this product maybe delayed up to two hours. May cause drowsiness. The product may impair the ability to drive or operate machinery. Please use extreme caution.</p>
  </div>

  <div class="notice notice--dosing">
    <h2 class="notice__title">DOSING:</h2>
    <p class="notice__body">The appropriate dose may be different for each person. Please consult your physician. Consume with care.</p>
  </div>

  <div class="nutrition">
    <div class="nutrition__title">Nutrition Facts</div>
    <div class="nutrition__row nutrition__row--thick"><span>Serving size</span><b>1 Piece(3g)</b></div>
    <div>Amount Per Serving</div>
    <div class="nutrition__cal"><span>Calories</span><strong>10</strong></div>
    <div class="nutrition__dv">%Daily Value*</div>
    <div class="nutrition__row"><span>Total Fat 0g</span><span>0%</span></div>
    <div class="nutrition__row nutrition__row--indent"><span>Saturated Fat 0g</span><span>0%</span></div>
    <div class="nutrition__row nutrition__row--indent"><i>Trans Fat 0g</i><span></span></div>
    <div class="nutrition__row"><span>Cholesterol 0g</span><span>0%</span></div>
    <div class="nutrition__row"><span>Sodium 0mg</span><span>0%</span></div>
    <div class="nutrition__row"><span>Total Carbhydrate 3g</span><span>1%</span></div>
    <div class="nutrition__row nutrition__row--indent"><span>Dietary fiber 0g</span><span>0%</span></div>
    <div class="nutrition__row nutrition__row--indent"><span>Total Sugars 2g</span><span></span></div>
    <div class="nutrition__row nutrition__row--indent"><span>Includes 2g Added Sugars</span><span>4%</span></div>
    <div class="nutrition__row nutrition__row--thick"><span>Protein 0g</span><span></span></div>
    <div class="nutrition__row"><span>Vitamin D 0mcg</span><span>0%</span></div>
    <div class="nutrition__row"><span>Calcium 0mg</span><span>0%</span></div>
    <div class="nutrition__row"><span>Iron 0mg</span><span>0%</span></div>
    <div class="nutrition__row"><span>Potassium 0mg</span><span>0%</span></div>
    <p class="nutrition__foot">*The % Daily Value (DV) tells you how much a nutrient in a serving of food contributes to a daily diet. 2,000 calories a day is used for general nutrition advice.</p>
  </div>

  <p class="ingredients">Ingredients:<br>Sugar, Tapioca Syrup, Water, Pectin, Citric Acid, Hemp Extract</p>

  <div class="brand brand--back"><span>Rare Plume</span><span>Edibles</span></div>
</section>

</body>
</html>
```